Create design for Dark Theme Website

We are a solar company wanting a website that has clean crisp feel of Quince. We like the dark contrasting theme in the Varnel Coreblock and Brightwick Dwelling Current websites listed below. We want a dark theme with single scroll down style page.
See the following for theme and look:
https://www.varnel.example/solarpanels
https://brightwickdwellingcurrent.example/

Our current website for further information is http://greyhollowsolar.example

We want the following sections on the single page as they scroll down:
1. Main Landing page for Grey Hollow Solar.
2. About us - company / service description
3. How it works - animation showing house with powerlines. The animations will show 'on-grid' day time, on-grid night time, Hybrid day time, Hybrid nightime / or stormy weather)
4. Mobile / monitoring - We like the brightwick photo style. We want to show our app on phone.
5. Home installation location - SHow location of installation and details about requirements
6. Solution Specifications Section- A button product filter, basic specs are shown on site (like varnel buy now) - really detailed information on brochure (like brightwick size selection)
7. Request Solutions Consultant form - if you want a quote, done in form style (Name, email, phone)
8. Estimator - (price estimator like varnel buy now) would have address finder, home bedroom count, install timeframe, contact details (first name, last name, email, phone, contact time preference)

I have uploaded our two brochures and some example diagrams for reference and image material.

Target Market(s)

Solar Energy Customers, wanting ongrid, off-grid or hybrid microgrids or solar energy solutions.

Industry/Entity Type

Solar Energy

Coding

Coded - Design and coding required

Number of Pages Required

1 page

Font styles to use
Sans Serif

Requirements
Must have
• The dark theme to match the company name and themes used by Varnel and Brightwick. Want a single scroll down page
Nice to have
• Nice transitions and animations to show different types of microgrid.

```html
<!DOCTYPE html>
<html lang="en">
<head>
<meta charset="utf-8">
<title>Grey Hollow Solar</title>
<link href="https://fonts.googleapis.com/css2?family=Poppins:ital,wght@0,400;0,500;0,600;1,400&display=swap" rel="stylesheet">
<style>
:root{
  --bg-mid:#333333;
  --bg-deep:#222222;
  --white:#ffffff;
  --green:#6aa621;
  --green-line:#527e24;
  --green-dot:#5b8c2a;
  --placeholder:#8a8a8a;
  --tab-text:#333333;
}
*{box-sizing:border-box;margin:0;padding:0}
html,body{width:1200px;height:2388px;overflow:hidden}
body{font-family:'Poppins',sans-serif;color:var(--white);background:var(--bg-mid);position:relative}
section,footer{position:absolute;left:0;width:1200px}
.abs{position:absolute}
h2{font-weight:600;font-size:25px;letter-spacing:.2px;text-transform:uppercase;line-height:1}

/* installation */
.install{top:0;height:447px;background:var(--bg-mid)}
.install h2{left:150px;top:110px}
.install .lead{left:150px;top:157px;width:340px;font-size:13.5px;line-height:20.5px}
.install ol{left:150px;top:230px;list-style:none;font-size:13.5px;line-height:27px}
.install .photo{left:600px;top:72px;width:449px;height:300px;background:linear-gradient(180deg,#dfe5e7 0%,#dfe5e7 22%,#2a3346 38%,#8c8478 60%,#6f6a5f 85%,#3e4430 100%)}

/* form cards */
.estimator{top:447px;height:634px;background:var(--bg-deep)}
.card{position:absolute;left:225px;width:749px;background:var(--bg-mid)}
.estimator .card{top:74px;height:486px}
.card h2{position:absolute;left:0;width:100%;text-align:center}
.field{position:absolute;width:319px;height:45px;background:var(--white);border:0;padding:0 14px;font-family:'Poppins',sans-serif;font-style:italic;font-size:13.5px;color:var(--placeholder);display:flex;align-items:center}
.field.message{width:675px;height:187px;align-items:flex-start;padding-top:10px}
.col-a{left:37px}.col-b{left:393px}
.submit{position:absolute;left:562px;width:150px;height:45px;background:var(--green);color:var(--white);font-family:'Poppins',sans-serif;font-weight:600;font-size:11.5px;border:0;display:flex;align-items:center;justify-content:center}

/* specifications */
.specs{top:1081px;height:536px;background:var(--bg-mid)}
.specs h2{left:0;width:100%;text-align:center;top:76px}
.tabs{position:absolute;top:126px;left:0;width:1200px;height:44px;background:var(--white)}
.tab{position:absolute;top:0;line-height:44px;font-size:12.5px;font-weight:500;color:var(--tab-text);transform:translateX(-50%);text-transform:uppercase}
.tab.active{color:var(--green)}
.plan h3{position:absolute;font-size:18.5px;font-weight:600}
.row{position:absolute;height:30px;display:flex;align-items:center}
.row .label{font-size:15px;font-weight:500;white-space:nowrap;padding-right:14px}
.row .rule{flex:1;height:2px;background:var(--green-line);margin-right:16px}
.row svg{flex:none}
.detail{position:absolute;font-size:13px;color:#d6d6d6}

/* quotation */
.quote{top:1617px;height:702px}
.quote .map{position:absolute;inset:0;background:linear-gradient(100deg,#5b6e5f 0%,#5d7061 28%,#4c5f7b 40%,#4c5f7b 78%,#586d5e 100%)}
.quote .card{top:81px;height:538px}

footer{top:2319px;height:69px;background:var(--bg-mid)}
footer .copy{left:151px;top:25px;font-size:13px;font-weight:500}
.social{position:absolute;top:12px;width:44px;height:44px;border-radius:50%;background:var(--green)}
</style>
</head>
<body>

<section class="install">
  <h2 class="abs">Installation &amp; Requirements</h2>
  <p class="abs lead">Integer maximus rutrum laoreet. Donec ut leo consectetur, feugiat urna sed, rhoncus magna. Curabitur ut efficitur est.</p>
  <ol class="abs">
    <li>1- MonoCrystalline PV Panels</li>
    <li>2- Solar &amp; DC Distribution Box</li>
    <li>3- Output Inverter that has Auto-Start Generator</li>
    <li>4- Lithium Battery</li>
  </ol>
  <div class="abs photo" role="img" aria-label="Photo of a two-storey shingled house with solar panels on a dark roof"></div>
</section>

<section class="estimator">
  <form class="card">
    <h2 style="top:36px">Price Estimator</h2>
    <div class="field col-a" style="top:88px">Address</div>
    <div class="field col-b" style="top:88px">Home Bedroom Count</div>
    <div class="field col-a" style="top:163px">Install Timeframe</div>
    <div class="field col-b" style="top:163px">E-mail</div>
    <div class="field col-a" style="top:246px">First Name</div>
    <div class="field col-b" style="top:246px">Last Name</div>
    <div class="field col-a" style="top:321px">Phone Number</div>
    <div class="field col-b" style="top:321px">Contact Time Preference</div>
    <div class="submit" style="top:403px">SUBMIT</div>
  </form>
</section>

<section class="specs">
  <h2 class="abs">Solution Specifications</h2>
  <nav class="tabs">
    <span class="tab" style="left:299px">Home</span>
    <span class="tab" style="left:424px">Large Home</span>
    <span class="tab" style="left:606px">Commercial Business</span>
    <span class="tab" style="left:776px">Grid-Tie</span>
    <span class="tab active" style="left:895px">Hybrid</span>
  </nav>

  <div class="plan">
    <h3 style="left:148px;top:188px">Hybrid 5KW</h3>
    <div class="row" style="left:150px;top:226px;width:412px"><span class="label">Inverter</span><span class="rule"></span><svg width="30" height="30" viewBox="0 0 30 30"><circle cx="15" cy="15" r="15" fill="#5b8c2a"/><path d="M10 13l5 5 5-5" fill="none" stroke="#fff" stroke-width="1.5"/></svg></div>
    <div class="row" style="left:150px;top:271px;width:412px"><span class="label">Panel</span><span class="rule"></span><svg width="30" height="30" viewBox="0 0 30 30"><circle cx="15" cy="15" r="15" fill="#5b8c2a"/><path d="M10 13l5 5 5-5" fill="none" stroke="#fff" stroke-width="1.5"/></svg></div>
    <div class="row" style="left:150px;top:316px;width:412px"><span class="label">Install Garantee</span><span class="rule"></span><svg width="30" height="30" viewBox="0 0 30 30"><circle cx="15" cy="15" r="15" fill="#5b8c2a"/><path d="M10 13l5 5 5-5" fill="none" stroke="#fff" stroke-width="1.5"/></svg></div>
    <div class="row" style="left:150px;top:361px;width:412px"><span class="label">Warranty on Panel Output</span><span class="rule"></span><svg width="30" height="30" viewBox="0 0 30 30"><circle cx="15" cy="15" r="15" fill="#5b8c2a"/><path d="M10 13l5 5 5-5" fill="none" stroke="#fff" stroke-width="1.5"/></svg></div>
    <div class="row" style="left:150px;top:406px;width:412px"><span class="label">Battery</span><span class="rule"></span><svg width="30" height="30" viewBox="0 0 30 30"><circle cx="15" cy="15" r="15" fill="#5b8c2a"/><path d="M10 17l5-5 5 5" fill="none" stroke="#fff" stroke-width="1.5"/></svg></div>
    <p class="detail" style="left:150px;top:441px">10 kWh Lithium Battery</p>
  </div>

  <div class="plan">
    <h3 style="left:636px;top:188px">Hybrid 8KW</h3>
    <div class="row" style="left:637px;top:226px;width:413px"><span class="label">Inverter</span><span class="rule"></span><svg width="30" height="30" viewBox="0 0 30 30"><circle cx="15" cy="15" r="15" fill="#5b8c2a"/><path d="M10 17l5-5 5 5" fill="none" stroke="#fff" stroke-width="1.5"/></svg></div>
    <p class="detail" style="left:637px;top:258px">8 kW Corvane Inverter</p>
    <div class="row" style="left:637px;top:294px;width:413px"><span class="label">Panel</span><span class="rule"></span><svg width="30" height="30" viewBox="0 0 30 30"><circle cx="15" cy="15" r="15" fill="#5b8c2a"/><path d="M10 13l5 5 5-5" fill="none" stroke="#fff" stroke-width="1.5"/></svg></div>
    <div class="row" style="left:637px;top:339px;width:413px"><span class="label">Install Garantee</span><span class="rule"></span><svg width="30" height="30" viewBox="0 0 30 30"><circle cx="15" cy="15" r="15" fill="#5b8c2a"/><path d="M10 13l5 5 5-5" fill="none" stroke="#fff" stroke-width="1.5"/></svg></div>
    <div class="row" style="left:637px;top:384px;width:413px"><span class="label">Warranty on Panel Output</span><span class="rule"></span><svg width="30" height="30" viewBox="0 0 30 30"><circle cx="15" cy="15" r="15" fill="#5b8c2a"/><path d="M10 13l5 5 5-5" fill="none" stroke="#fff" stroke-width="1.5"/></svg></div>
    <div class="row" style="left:637px;top:429px;width:413px"><span class="label">Battery</span><span class="rule"></span><svg width="30" height="30" viewBox="0 0 30 30"><circle cx="15" cy="15" r="15" fill="#5b8c2a"/><path d="M10 13l5 5 5-5" fill="none" stroke="#fff" stroke-width="1.5"/></svg></div>
  </div>
</section>

<section class="quote">
  <div class="map" role="img" aria-label="Map of the installation region showing coastline, towns and roads"></div>
  <form class="card">
    <h2 style="top:36px">Request Quotation</h2>
    <div class="field col-a" style="top:88px">First Name</div>
    <div class="field col-b" style="top:88px">Last Name</div>
    <div class="field col-a" style="top:163px">Email</div>
    <div class="field col-b" style="top:163px">Phone Number</div>
    <div class="field message col-a" style="top:238px">Message</div>
    <div class="submit" style="top:456px">SUBMIT</div>
  </form>
</section>

<footer>
  <p class="abs copy">© Grey Hollow Solar 2020 All Rights Reserved.</p>
  <span class="social" style="left:771px" aria-label="Chat profile"></span>
  <span class="social" style="left:830px" aria-label="Professional network profile"></span>
  <span class="social" style="left:887px" aria-label="Video channel"></span>
  <span class="social" style="left:947px" aria-label="Microblog profile"></span>
  <span class="social" style="left:1004px" aria-label="Social network page"></span>
</footer>

</body>
</html>
```